【依頼の目的/概要】
電子書籍(lumora)の表紙デザインをお願いします。
【画像サイズ】※QMSより抜粋
表紙ファイルの理想的な寸法は2560×1600ピクセルです。
注:画像の寸法は1000×625ピクセル以上であることが必要です。
画像の最大の寸法は10000×10000ピクセルです。

【タイトル】
「森と響きあう内なる治癒の道」
サブキャッチ
「もうガンもウイルスも怖くない」 「30年の医療現場で私が感じたこと」
「輝く人生を送るための幸せ健康学」「歴史とデータから浮かび上がる真実」など。
【著者】
看護師30年
堀田みき

【本の内容】
病院や薬に依存し続けてきた結果の日本の現状を歴史やデータから検証。
西洋医学以前の医療に着目し自然免疫の力で健康を取り戻せることが出来ることをお伝えした本です。
※本文を参考資料として添付します。

【デザイン要望】
内容が少し専門的なのですが特に一般の方に読んでいただきたいのであまり堅苦しくない印象のものを考えてはいますが、特に要望はありませんので自由な発想でのご応募を楽しみにしています。
※次点 次々点の方への参加報酬を設定いたしました。
※その他、必要な情報がありましたらお問い合わせください。
宜しくお願いいたします。

どの作品も本当に素晴らしく最後まで悩みに悩みました。内容は医療系なのですが特に一般の方に手にとっていただきたいことから表紙と内容のギャップがないものをと思うとデザインが気に入っても、本の内容で表紙のイメージと全然違うとガッカリされないかなど考え非常に悩みました。タイトルとサブキャッチの大きさや色使い、堅苦しくない明るいデザインが私のイメージと合いましたのでtorvel様のデザインを選ばせていただきました。

今回ピクモアさんに初めて表紙の依頼をさせていただきました。デザイナーさんたちのレベルの高さに感動しておりました。
どのデザインもそれぞれが個性的で本当に素晴らしく最後の最後まで迷っておりました。
今回の本の内容と、専門的ではあるのですが一般向けにしたいということで悩んだ末そちらの視点から一点決めさせていただきました。
1点しか選べないことが心苦しいです。
皆さまお忙しい中、貴重なお時間を割いていただき本当にありがとうございました。
心から感謝しております。

```html
<!DOCTYPE html>
<html lang="ja">
<head>
<meta charset="utf-8">
<title>森と響きあう内なる治癒の道 表紙</title>
<link href="https://fonts.googleapis.com/css2?family=M+PLUS+1p:wght@500;700;800;900&family=Noto+Sans+JP:wght@400;500;700&display=swap" rel="stylesheet">
<style>
  :root {
    --space-deep: #05070d;
    --space-mid: #141a26;
    --glow-blue: #4d7fc4;
    --glow-white: #e8f2ff;
    --title-ink: #141414;
    --title-accent: #d8261b;
    --big-orange: #f07a12;
    --paper: #ffffff;
    --ink: #1a1a1a;
    --emph-red: #e02a1f;
    --bubble: #d5ecf7;
    --bubble-ink: #2f3a44;
    --band: #fbd9bf;
    --band-ink: #ffffff;
    --figure-tone: #e7eef3;
  }
  html, body {
    margin: 0;
    padding: 0;
    width: 750px;
    height: 1200px;
    overflow: hidden;
    background: var(--paper);
  }
  .cover {
    position: relative;
    width: 750px;
    height: 1200px;
    overflow: hidden;
    background: var(--paper);
    font-family: "Noto Sans JP", sans-serif;
  }
  .space-scene {
    position: absolute;
    left: 0; top: 0;
    width: 750px; height: 790px;
    background:
      radial-gradient(ellipse 520px 140px at 375px 665px, rgba(232,242,255,0.95) 0%, rgba(120,170,230,0.7) 30%, rgba(40,70,120,0.25) 65%, rgba(0,0,0,0) 100%),
      radial-gradient(ellipse 900px 420px at 375px 900px, #0d1422 0%, #0b1019 60%, rgba(0,0,0,0) 61%),
      radial-gradient(circle at 375px 380px, #2a3140 0%, var(--space-mid) 45%, var(--space-deep) 100%);
  }
  .title {
    position: absolute;
    left: 0; width: 750px;
    margin: 0;
    text-align: center;
    font-family: "M PLUS 1p", sans-serif;
    font-weight: 900;
    color: var(--title-ink);
    -webkit-text-stroke: 0;
    text-shadow: 0 0 6px rgba(255,255,255,0.9), 0 0 2px #fff;
  }
  .title-line {
    position: absolute;
    left: 0; width: 750px;
    display: block;
    font-size: 74px;
    letter-spacing: 2px;
    line-height: 1;
  }
  .title-line.first { top: 175px; }
  .title-line.second { top: 278px; }
  .title-line .accent { color: var(--title-accent); }
  .title-big {
    position: absolute;
    left: 0; width: 750px;
    top: 480px;
    display: block;
    font-size: 200px;
    line-height: 1;
    color: var(--big-orange);
    text-shadow: 0 0 10px rgba(255,200,120,0.6);
  }
  .catch {
    position: absolute;
    left: 60px; top: 785px;
    margin: 0;
    font-family: "M PLUS 1p", sans-serif;
    font-weight: 700;
    color: var(--ink);
    font-size: 34px;
    line-height: 1.4;
  }
  .catch span { display: block; }
  .catch .l1 { padding-left: 0; }
  .catch .l2 { padding-left: 62px; }
  .catch .l3 { padding-left: 188px; }
  .catch em {
    font-style: normal;
    text-emphasis: filled dot var(--emph-red);
    -webkit-text-emphasis: filled dot var(--emph-red);
    text-emphasis-position: over right;
    -webkit-text-emphasis-position: over right;
  }
  .bubble {
    position: absolute;
    left: 463px; top: 720px;
    width: 272px; height: 230px;
    border-radius: 50%;
    background: var(--bubble);
    display: flex;
    flex-direction: column;
    align-items: center;
    justify-content: center;
    font-family: "M PLUS 1p", sans-serif;
    color: var(--bubble-ink);
    font-weight: 700;
    line-height: 1.35;
    text-align: center;
  }
  .bubble .years { font-size: 34px; letter-spacing: 2px; }
  .bubble .years small { font-size: 24px; }
  .bubble .rest { font-size: 25px; }
  .band {
    position: absolute;
    left: 25px;
    width: 420px;
    background: linear-gradient(90deg, var(--band) 0%, var(--band) 70%, rgba(251,217,191,0.6) 100%);
    color: var(--band-ink);
    font-family: "M PLUS 1p", sans-serif;
    font-weight: 700;
    font-size: 23px;
    line-height: 1.4;
    padding: 8px 16px;
    box-sizing: border-box;
  }
  .band.happy { top: 945px; height: 82px; }
  .band.truth { top: 1025px; height: 82px; }
  .band .key {
    display: block;
    text-align: right;
    color: var(--emph-red);
    text-decoration: underline;
    text-underline-offset: 4px;
  }
  .figure {
    position: absolute;
    left: 505px; top: 940px;
    width: 220px; height: 215px;
    background: linear-gradient(180deg, #ffffff 0%, var(--figure-tone) 100%);
    border-radius: 12px;
  }
  .author {
    position: absolute;
    left: 505px; top: 1160px;
    margin: 0;
    font-size: 22px;
    color: var(--ink);
    font-family: "Noto Sans JP", sans-serif;
    font-weight: 500;
  }
</style>
</head>
<body>
<main class="cover">
  <div class="space-scene" role="img" aria-label="夜空の宇宙と光に縁取られた地球の地平線"></div>

  <h1 class="title">
    <span class="title-line first">森と響きあう</span>
    <span class="title-line second">内なる<span class="accent">治癒</span>の</span>
    <span class="title-big">道</span>
  </h1>

  <p class="catch">
    <span class="l1">もう</span>
    <span class="l2"><em>ガン</em>も<em>ウイルス</em>も</span>
    <span class="l3">怖くない！</span>
  </p>

  <div class="bubble">
    <span class="years">３０年<small>の</small></span>
    <span class="rest">医療現場で</span>
    <span class="rest">私が感じたこと</span>
  </div>

  <div class="band happy">
    輝く人生を送るための
    <span class="key">幸せ健康学</span>
  </div>
  <div class="band truth">
    歴史とデータから浮かび上がる
    <span class="key">真実</span>
  </div>

  <div class="figure" role="img" aria-label="指を立てて語りかける看護師のイラスト"></div>

  <p class="author">著・堀田みき</p>
</main>
</body>
</html>
```